Bref créative
Brisk Haulage Web Page
Brisk Haulage
Energy
Energy services company in the business of storing, transporting and handling the logistics of oilfield liquids (water, brine, oil, etc.)
Looking for an elegant site - not too busy and distracting.
left side
see our logo and incorporate it.
Brisk Haulage Logo
Brisk Haulage Logo .gif

```html
<!DOCTYPE html>
<html lang="en">
<head>
<meta charset="utf-8">
<title>Brisk Haulage</title>
<link href="https://fonts.googleapis.com/css2?family=Arimo:wght@400;700&display=swap" rel="stylesheet">
<style>
:root{
  --blue:#1f7fc4;
  --blue-light:#5ab4ea;
  --orange:#e8801a;
  --ink:#333;
  --muted:#777;
  --line:#d9d9d9;
  --panel:#f4f4f4;
  --black:#0d0d0d;
  --footer-text:#bbb;
}
*{box-sizing:border-box;margin:0;padding:0}
html,body{width:1200px;height:1009px;overflow:hidden}
body{font-family:"Arimo",Arial,sans-serif;color:var(--ink);background:linear-gradient(#d6d9dc 0,#eef0f1 150px,#fff 505px);position:relative}
.page{position:absolute;left:183px;width:834px}
.header{top:14px;height:136px;background:linear-gradient(#fff,#f1f2f3);box-shadow:0 0 6px rgba(0,0,0,.15)}
.brand{position:absolute;left:24px;top:36px;display:flex;align-items:center;gap:12px}
.brand-dot{width:40px;height:40px;border-radius:50%;background:var(--blue)}
.brand-name{font-size:30px;font-weight:700;color:var(--blue);letter-spacing:.5px}
.call{position:absolute;right:24px;top:20px;font-size:14px;color:var(--orange);display:flex;align-items:center;gap:8px}
.nav{position:absolute;right:20px;top:104px;display:flex;background:linear-gradient(#f7f7f7,#e4e4e4);border:1px solid var(--line);height:30px}
.nav a{font-size:12px;font-weight:700;color:#444;text-decoration:none;padding:0 18px;line-height:28px}
.nav a.active{color:var(--blue);background:#fff}
.hero{position:absolute;left:0;top:150px;width:1200px;height:355px;background:linear-gradient(#2f6e9c 0%,#5f99c2 40%,#9fc3dd 70%,#3f7fae 100%)}
.caption{position:absolute;left:183px;top:300px;width:834px;height:50px;background:rgba(0,0,0,.8);font-size:17px;line-height:20px;font-weight:700;color:#fff;padding:15px 10px;white-space:nowrap;overflow:hidden}
.caption span{color:var(--blue-light)}
.boxes{top:545px;display:flex;gap:14px}
.box{flex:1;height:142px;border:1px solid var(--line);background:var(--panel);padding:12px 14px;position:relative}
.box h2{font-size:24px;font-weight:400;color:var(--blue);margin-bottom:10px}
.box p{font-size:11px;line-height:15px;color:var(--muted)}
.box.about{display:grid;grid-template-columns:70px 1fr}
.box.about h2{grid-column:1/3}
.about-mark{width:54px;height:54px;border-radius:50%;background:var(--blue)}
.more{position:absolute;right:14px;bottom:12px;font-size:11px;color:#333;border-bottom:1px solid #999;padding:0 4px}
.news{top:709px;height:34px;border:1px solid var(--line);background:var(--panel);display:flex;align-items:center;padding:0 12px;font-size:10px;color:var(--muted);gap:18px}
.news h3{font-size:16px;font-weight:400;color:var(--blue)}
.news .all{margin-left:auto;font-size:11px;color:#333;text-decoration:underline}
.footer{position:absolute;left:0;top:796px;width:1200px;height:164px;background:var(--black)}
.footer-cols{position:absolute;left:195px;top:30px;width:820px;display:flex}
.col{flex:1}
.col h4{font-size:11px;font-weight:700;color:#fff;margin-bottom:12px}
.col li{list-style:none;font-size:9px;color:var(--footer-text);border-bottom:1px solid #333;padding:5px 0;width:120px}
.col p{font-size:9px;line-height:14px;color:var(--footer-text);width:120px}
.bottom{position:absolute;left:195px;top:975px;width:810px;display:flex;align-items:center;font-size:10px;color:#555}
.social{margin-left:auto;display:flex;gap:6px}
.social i{width:22px;height:22px;border-radius:4px;display:block}
</style>
</head>
<body>
<header class="page header">
  <div class="brand"><span class="brand-dot"></span><span class="brand-name">Brisk Haulage</span></div>
  <div class="call">
    <svg width="18" height="14" viewBox="0 0 18 14"><path d="M2 5c0-3 14-3 14 0l-3 1-1-2H6L5 6z" fill="#333"/><rect x="4" y="7" width="10" height="6" rx="1" fill="#333"/></svg>
    CALL US: 555 010 2040
  </div>
  <nav class="nav">
    <a class="active">HOME</a><a>ABOUT US</a><a>OUR SERVICES</a><a>NEWS</a><a>LINKS</a><a>GALLERY</a><a>CONTACT</a>
  </nav>
</header>

<section class="hero" role="img" aria-label="Wind turbines against a blue sky with water waves at the edges">
  <div class="caption">The team of experts and professionals <span>Water, Waste water and Energy Sector in your place</span></div>
</section>

<section class="page boxes">
  <article class="box">
    <h2>Water Services</h2>
    <p>We move and store water, brine and oil for oilfield sites across the region, with tanks and trucks ready day and night.</p>
    <span class="more">Learn more</span>
  </article>
  <article class="box">
    <h2>Energy</h2>
    <p>Our energy team handles the logistics of field liquids from well to disposal, keeping every load safe, tracked and on time.</p>
    <span class="more">Learn more</span>
  </article>
  <article class="box about">
    <h2>About us</h2>
    <span class="about-mark"></span>
    <p>Brisk Haulage is a trusted name in the storing and transport of liquids for the energy sector.</p>
    <span class="more">Learn more</span>
  </article>
</section>

<section class="page news">
  <h3>News and events</h3>
  <span>New water transfer yard opens this spring &nbsp;· May 07, 2011</span>
  <span>Fleet grows by ten new tank trucks &nbsp;· May 07, 2011</span>
  <a class="all">View all</a>
</section>

<footer class="footer">
  <div class="footer-cols">
    <div class="col"><h4>OUR SERVICES</h4><ul><li>Hot Shot Services</li><li>Frac Tank Rentals</li><li>Fluid Transfers</li><li>Pre-Job Site Preparation</li></ul></div>
    <div class="col"><h4>ABOUT US</h4><ul><li>Experience</li><li>Work Process</li><li>Technical Data</li><li>Management</li></ul></div>
    <div class="col"><h4>WATER</h4><ul><li>Water Services</li><li>Water Treatment Options</li><li>Produced Water</li><li>Storm Water Handling</li></ul></div>
    <div class="col"><h4>ENERGY</h4><ul><li>Field Fluids Hauling</li><li>Brine Disposal</li><li>Alternative Energy</li><li>Thermal Power</li></ul></div>
    <div class="col"><h4>CONTACT US</h4><p>Call or write to our team for quotes, bookings and site visits across the energy sector.</p></div>
  </div>
</footer>

<div class="bottom">
  <span>© 2012 Brisk Haulage. All rights reserved.</span>
  <div class="social"><i style="background:#4aa8e0"></i><i style="background:#e8801a"></i><i style="background:#3b5b98"></i><i style="background:#c4302b"></i></div>
</div>
</body>
</html>
```